Honigetikett gesucht
Zielgruppe
Ich bin ein Hobbyimker und brauche ein Etikett für meinen Honig. Zielgruppe = Jeder
Aufgabenstellung
Bitte keine schwarzen Etiketten mehr... gefällt uns leider nicht. Danke!
Das Etikett ist für Honig, 500 Gramm Glas. Man muss den gesetzlichen Vorgaben einhalten. https://www.wabenhofportal.at/de/labor/lebensmittelrecht.html
Blütenhonig aus Österreich
Name
Adresse
500 g
Trocken und vor Licht und Wärme geschützt lagern.
Mindestens haltbar bis:
Sichtfeldregelung
Sachbezeichnung und Nettofüllmenge müssen am Etikett in einem Sichtfeld angebracht werden. Ein Sichtfeld ist eine Oberfläche einer Verpackung, die von einem einzigen Blickpunkt aus gelesen werden kann.
Mindesthaltbarkeitsdatum und Lagerbedingungen sind in einem Sichtfeld anzubringen. Dabei muss die Lagerbedingung über oder unter der Haltbarkeit angeführt werden und darf nicht durch Bild- oder Schrift getrennt sein.
Mindestschriftgröße aller verpflichtenden Angaben (Ausnahme Nettofüllmenge) Mindestschriftgröße:
Die verwendete Schrift muss am kleinen „x“ der verwendeten Schriftart gemessen mindestens 1,2mm Höhe ausmachen
Erreicht die Gesamtoberfläche des Gebindes auf dem Ein Etikett angebracht werden kann max. 80cm2, so muss die Höhe am kleinen „x“ der verwendeten Schriftart gemessen mindestens 0,9mm Höhe ausmachen (beim Honigglas wäre dies erst unter dem 125g Glas)
Die Mindestschriftgröße der Nettofüllmenge bleibt davon unberührt und unterliegt weiterhin der Fertigpackungsverordnung (siehe Nettofüllmenge)

```html
<!DOCTYPE html>
<html lang="de">
<head>
<meta charset="utf-8">
<title>Blütenhonig – Etikett</title>
<link rel="stylesheet" href="https://fonts.googleapis.com/css2?family=Crimson+Text:wght@400;600&display=swap">
<style>
  :root {
    --backdrop: #f1d3c0;
    --label-white: #ffffff;
    --label-tint: #f3f2ee;
    --honey-gold: #d8bc6c;
    --honey-gold-light: #e6cd80;
    --gold-text: #c9a94f;
    --ink: #4a4a4a;
    --ink-soft: #5a5a5a;
  }
  * { margin: 0; padding: 0; box-sizing: border-box; }
  html, body {
    width: 1200px;
    height: 1200px;
    overflow: hidden;
    background: var(--backdrop);
    font-family: "Crimson Text", "Palatino Linotype", serif;
  }
  .canvas {
    position: relative;
    width: 1200px;
    height: 1200px;
  }
  .label {
    position: absolute;
    left: 50px;
    top: 290px;
    width: 1100px;
    height: 620px;
    background: var(--label-white);
    overflow: hidden;
    box-shadow: 0 10px 30px rgba(120, 70, 40, 0.12);
  }
  .label__pattern {
    position: absolute;
    inset: 0;
    background: linear-gradient(90deg, var(--label-tint) 0%, var(--label-white) 70%);
  }
  .label__band {
    position: absolute;
    left: 0;
    top: 0;
    width: 100%;
    height: 200px;
    background: linear-gradient(90deg, var(--honey-gold) 0%, var(--honey-gold-light) 100%);
  }
  .legal-panel {
    position: absolute;
    left: 24px;
    top: 255px;
    width: 170px;
    color: var(--ink-soft);
    font-size: 17px;
    line-height: 1.2;
  }
  .legal-panel p { margin-bottom: 14px; }
  .legal-panel .producer { margin-top: 58px; }
  .legal-panel strong { font-weight: 600; }
  .front-panel {
    position: absolute;
    left: 300px;
    top: 320px;
    width: 540px;
    text-align: center;
  }
  .product-name {
    font-size: 92px;
    font-weight: 400;
    color: var(--ink);
    line-height: 1;
    letter-spacing: 1px;
  }
  .name-rule {
    width: 410px;
    height: 4px;
    margin: 18px auto 20px;
    background: var(--gold-text);
  }
  .tagline {
    font-size: 31px;
    color: var(--ink-soft);
    letter-spacing: 0.5px;
  }
  .net-weight {
    margin-top: 8px;
    font-size: 66px;
    color: var(--gold-text);
    line-height: 1.1;
  }
  .net-weight .estimated-sign {
    font-size: 44px;
    margin-right: 6px;
  }
</style>
</head>
<body>
  <main class="canvas">
    <section class="label">
      <div class="label__pattern" role="img" aria-label="Dezentes Wabenmuster in hellem Grau auf weißem Grund"></div>
      <div class="label__band" role="img" aria-label="Goldfarbenes Honigband am oberen Etikettrand"></div>

      <div class="legal-panel">
        <p>Mindestens haltbar bis: <strong>09/2023</strong></p>
        <p>Trocken und vor Licht und Wärme geschützt lagern.</p>
        <p class="producer">Ilse Tomberger<br>Birkenfeldgasse 4b<br>8010 Graz<br>i.tomberger@postfeld.at</p>
      </div>

      <div class="front-panel">
        <h1 class="product-name">Blütenhonig</h1>
        <div class="name-rule"></div>
        <p class="tagline">Spitzenqualität aus Österreich</p>
        <p class="net-weight"><span class="estimated-sign">℮</span>500g</p>
      </div>
    </section>
  </main>
</body>
</html>
```